Current website re-design to a updated look and feel.

We currently have a website www.brightlanefreight.com that we want to give an updated look and feel to. We are a logistics company that competes with Harbex, Dm Whitfield, Tarn but on a smaller scale. We want something fresh and updated. We have two locations one in downtown Chicago, IL and one in Palatine IL. We are a fun group that also gets the job done. We know we need pictures of both locations and possibly a video, but we need fresh design ideas. The 'who we are' page is really the only page that we currently want to keep. The 'what we do' page needs to be completely re-done from a look and feel for sure.

Target Market(s)

Anyone who uses Truck transportation to move their product. Mainly US manufacturers.

Industry/Entity Type

Logistics

Number of Pages Required

5+ page

Font styles to use
Sans Serif

Colors
5c91c4
0355a3
d0dfed

Requirements
Must have
• The new design must entice people to want to do business with us. The design must have locations for pictures and at least one video which we know we will have to provide. Design must be easy to navigate.

```html
<!DOCTYPE html>
<html lang="en">
<head>
<meta charset="utf-8">
<title>Brightlane Freight – Transportation &amp; Distribution</title>
<link href="https://fonts.googleapis.com/css2?family=Open+Sans:wght@400;600;700;800&family=Oswald:wght@500;700&display=swap" rel="stylesheet">
<style>
:root{
  --blue:#0355a3;
  --blue-mid:#5c91c4;
  --blue-pale:#d0dfed;
  --orange:#f7941d;
  --ink:#333;
  --grey:#777;
  --line:#e2e2e2;
  --dark:#1f2a35;
  --footer:#22313f;
}
*{box-sizing:border-box;margin:0;padding:0}
html,body{width:1200px;height:2584px;overflow:hidden}
body{font-family:"Open Sans",Arial,sans-serif;color:var(--ink);background:#fff;position:relative}
.wrap{width:1040px;margin:0 auto;position:relative}

/* header */
.site-header{height:112px}
.site-header .wrap{height:112px;display:flex;align-items:center;justify-content:space-between}
.brand{display:flex;align-items:center;gap:12px;font-weight:800;font-size:30px;color:var(--blue)}
.brand-mark{width:26px;height:26px;background:var(--orange);border-radius:50%}
.header-contact{display:flex;align-items:center;gap:18px}
.phone{display:flex;align-items:center;gap:10px;font-size:13px;color:var(--grey)}
.phone strong{font-size:22px;color:var(--blue);font-weight:700}
.phone-icon{width:34px;height:34px;border:2px solid var(--orange);border-radius:50%;display:flex;align-items:center;justify-content:center}
.btn{display:inline-block;background:var(--orange);color:#fff;font-weight:700;font-size:13px;text-transform:uppercase;padding:10px 26px;border-radius:3px;letter-spacing:.5px}

/* nav */
.main-nav{height:48px;background:var(--blue)}
.main-nav ul{list-style:none;display:flex;height:48px;width:1040px;margin:0 auto}
.main-nav li{flex:1;display:flex;align-items:center;justify-content:center;color:#fff;font-size:13px;font-weight:700;text-transform:uppercase;border-right:1px solid rgba(255,255,255,.15)}
.main-nav li.active{background:var(--orange);flex:.7}

/* hero */
.hero{height:450px;position:relative;background:linear-gradient(180deg,#7aa7d1 0%,#4d7390 45%,#6b5a4a 75%,#3f3a33 100%);display:flex;flex-direction:column;align-items:center;justify-content:center}
.hero h1{font-family:Oswald,sans-serif;font-size:56px;line-height:1.1;color:#fff;text-align:center;text-transform:uppercase;letter-spacing:1px;text-shadow:0 2px 6px rgba(0,0,0,.4)}
.play{margin-top:26px;width:92px;height:92px}
.dots{position:absolute;bottom:22px;display:flex;gap:10px}
.dots span{width:10px;height:10px;border-radius:50%;background:rgba(255,255,255,.5)}
.dots span.on{background:#fff}

/* what we do */
.services{height:480px;background:#f4f6f8;padding-top:44px;text-align:center}
.section-title{font-size:30px;font-weight:800;color:var(--ink);text-transform:uppercase}
.rule{width:60px;height:3px;background:var(--orange);margin:10px auto 16px}
.lede{width:640px;margin:0 auto;font-size:13px;line-height:1.6;color:var(--grey)}
.cards{display:flex;justify-content:space-between;width:1040px;margin:40px auto 0}
.card{width:242px;height:250px;background:#fff;border:1px solid var(--line);padding:62px 22px 0;position:relative;text-align:center}
.card .icon{position:absolute;top:-36px;left:50%;margin-left:-44px;width:88px;height:88px}
.card h3{font-size:13px;font-weight:800;color:var(--ink);text-transform:uppercase;margin-bottom:10px}
.card p{font-size:12px;line-height:1.6;color:var(--grey)}
.card .more{display:block;margin-top:12px;font-size:11px;color:var(--orange);text-decoration:underline;font-weight:600}
.card.featured{background:var(--blue);border-color:var(--blue)}
.card.featured h3,.card.featured p{color:#fff}
.card.featured .more{color:#fff}

/* founder */
.founder{height:330px;background:linear-gradient(90deg,#2b2420,#4a3b30 50%,#2e2a27);color:#fff;padding-top:40px}
.founder h2{font-size:30px;font-weight:800;text-align:center;text-transform:uppercase}
.founder .rule{margin-bottom:28px}
.founder .body{width:760px;font-size:12.5px;line-height:1.7;color:#e6e6e6}
.founder .body p+p{margin-top:12px}
.founder .callout{margin-top:14px;color:var(--orange);font-weight:700;font-size:11.5px;text-transform:uppercase}
.founder-photo{position:absolute;right:10px;top:-6px;width:180px;height:180px;border-radius:50%;border:5px solid #fff;background:linear-gradient(160deg,#e7c48a,#b88a58 60%,#6b4b33)}

/* vision */
.vision{height:380px;padding-top:56px;text-align:center}
.vision .section-title{font-size:26px}
.cols{display:flex;justify-content:space-between;margin-top:30px;text-align:left}
.col{width:490px;display:flex;gap:18px}
.col svg{flex:0 0 54px}
.col h4{font-size:12px;font-weight:800;text-transform:uppercase;color:var(--ink)}
.col .sub{font-size:10px;color:var(--grey);margin-bottom:8px}
.col p{font-size:12px;line-height:1.7;color:var(--grey)}
.col p em{color:var(--orange);font-style:normal;font-weight:700}
.vision .btn{margin-top:44px;border-radius:22px;padding:13px 34px}

/* footer */
.footer-main{height:700px;background:linear-gradient(180deg,#1f2d3a 0%,#26384a 45%,#3b5670 75%,#2a3f54 100%);color:#fff;padding-top:40px}
.footer-main .wrap{display:flex;justify-content:space-between}
.updates{width:500px}
.updates h2{font-size:30px;font-weight:800;text-transform:uppercase}
.updates p{font-size:12px;line-height:1.6;color:#cfd8e1;margin:10px 0 24px}
.field{height:34px;background:#fff;border-radius:2px;margin-bottom:10px;font-size:12px;color:#999;padding:9px 12px;width:330px}
.updates .btn{margin-top:8px}
.contact{width:400px}
.contact h5{font-size:13px;font-weight:800;text-transform:uppercase;padding-bottom:8px;border-bottom:1px solid rgba(255,255,255,.3);margin-bottom:14px}
.contact li{list-style:none;display:flex;align-items:center;gap:12px;font-size:12.5px;margin-bottom:14px;color:#e6edf3}
.contact li span.ic{width:22px;height:22px;border-radius:50%;background:var(--orange);flex:0 0 22px}
.support{margin-top:26px}
.badges{display:flex;gap:16px}
.badge{width:180px;height:80px;background:#fff;border-radius:2px}
.ship{position:absolute;left:0;right:0;bottom:0;height:260px}

.footer-bottom{position:absolute;left:0;right:0;top:2500px;height:84px;background:#fff;text-align:center;padding-top:12px}
.social{display:flex;justify-content:center;gap:8px}
.social span{width:20px;height:20px;border-radius:50%;background:var(--blue)}
.foot-nav{margin-top:10px;font-size:10px;color:#555;display:flex;justify-content:center;gap:22px;text-transform:uppercase;font-weight:600}
.copy{margin-top:6px;font-size:9px;color:#999}
</style>
</head>
<body>

<header class="site-header">
  <div class="wrap">
    <div class="brand"><span class="brand-mark"></span>Brightlane Freight</div>
    <div class="header-contact">
      <div class="phone">
        <span class="phone-icon"><svg width="16" height="16" viewBox="0 0 24 24"><path d="M6.6 10.8a15 15 0 006.6 6.6l2.2-2.2c.3-.3.7-.4 1-.2 1.1.4 2.3.6 3.6.6.6 0 1 .4 1 1V20c0 .6-.4 1-1 1A17 17 0 013 4c0-.6.4-1 1-1h3.5c.6 0 1 .4 1 1 0 1.3.2 2.5.6 3.6.1.3 0 .7-.2 1z" fill="#f7941d"/></svg></span>
        Office Phone <strong>847.555.0142</strong>
      </div>
      <span class="btn">Log In</span>
    </div>
  </div>
</header>

<nav class="main-nav">
  <ul>
    <li class="active">Home</li><li>What We Do</li><li>How We Do It</li><li>Who We Are</li><li>Tracking</li><li>Chat</li><li>Contact</li>
  </ul>
</nav>

<section class="hero" role="img" aria-label="Photo of a container port with stacked shipping containers and cranes">
  <h1>Transportation &amp;<br>Distribution</h1>
  <svg class="play" viewBox="0 0 92 92"><circle cx="46" cy="46" r="43" fill="rgba(0,0,0,.25)" stroke="#fff" stroke-width="3"/><path d="M37 29l25 17-25 17z" fill="#fff"/></svg>
  <div class="dots"><span></span><span class="on"></span><span></span></div>
</section>

<section class="services">
  <h2 class="section-title">What We Do</h2>
  <div class="rule"></div>
  <p class="lede">We move freight for manufacturers across the country with care, speed and a crew that answers the phone. From a single pallet to full truckloads, we plan the route and keep you posted.</p>
  <div class="cards">
    <div class="card featured">
      <svg class="icon" viewBox="0 0 88 88"><rect x="4" y="4" width="80" height="80" transform="rotate(45 44 44)" fill="#f7941d"/><rect x="30" y="28" width="28" height="32" rx="2" fill="none" stroke="#fff" stroke-width="3"/><path d="M36 38h16M36 45h16M36 52h10" stroke="#fff" stroke-width="3"/></svg>
      <h3>Freight Management</h3>
      <p>We plan, book and track every load so your team can focus on building product.</p>
      <span class="more">Freight Management</span>
    </div>
    <div class="card">
      <svg class="icon" viewBox="0 0 88 88"><rect x="4" y="4" width="80" height="80" transform="rotate(45 44 44)" fill="#5c91c4"/><rect x="24" y="34" width="26" height="18" fill="#fff"/><path d="M50 38h9l6 7v7H50z" fill="#fff"/><circle cx="32" cy="55" r="4" fill="#fff"/><circle cx="58" cy="55" r="4" fill="#fff"/></svg>
      <h3>Transportation</h3>
      <p>Truckload, partial and less than truckload shipping on lanes across the country.</p>
      <span class="more">Transportation</span>
    </div>
    <div class="card">
      <svg class="icon" viewBox="0 0 88 88"><rect x="4" y="4" width="80" height="80" transform="rotate(45 44 44)" fill="#5c91c4"/><path d="M44 26l16 8v18l-16 8-16-8V34z" fill="#fff"/><path d="M28 34l16 8 16-8M44 42v18" stroke="#5c91c4" stroke-width="2" fill="none"/></svg>
      <h3>Warehouse &amp; Distribution</h3>
      <p>Secure storage and fast pick, pack and ship from our two Illinois locations.</p>
      <span class="more">Warehouse &amp; Distribution</span>
    </div>
    <div class="card">
      <svg class="icon" viewBox="0 0 88 88"><rect x="4" y="4" width="80" height="80" transform="rotate(45 44 44)" fill="#5c91c4"/><rect x="22" y="34" width="30" height="18" fill="#fff"/><path d="M52 38h10l5 7v7H52z" fill="#fff"/><circle cx="30" cy="55" r="4" fill="#fff"/><circle cx="60" cy="55" r="4" fill="#fff"/></svg>
      <h3>Carriers</h3>
      <p>Join our carrier network for steady loads, fair rates and quick pay.</p>
      <span class="more">Carriers</span>
    </div>
  </div>
</section>

<section class="founder" role="img" aria-label="Dark background photo of an office workspace">
  <h2>Welcome From Our Founder</h2>
  <div class="rule"></div>
  <div class="wrap">
    <div class="body">
      <p>Brightlane Freight started with one desk, one phone and a promise to treat every shipment like our own. Today our team in Chicago and Palatine still lives by that promise, and we have fun doing it.</p>
      <p>We believe logistics should be simple. You tell us what needs to move, and we handle the carriers, the paperwork and the updates so your freight arrives safely, on time and on budget.</p>
      <p class="callout">Let us take the worry out of your shipping. Call us today for a fast, friendly quote.</p>
    </div>
    <div class="founder-photo" role="img" aria-label="Portrait photo of the company founder"></div>
  </div>
</section>

<section class="vision">
  <div class="wrap">
    <h2 class="section-title">Brightlane Freight Vision and Mission</h2>
    <div class="rule"></div>
    <div class="cols">
      <div class="col">
        <svg width="54" height="54" viewBox="0 0 54 54"><rect x="4" y="24" width="10" height="24" fill="#777"/><path d="M16 26l10-18c3 0 5 2 4 6l-2 8h14c3 0 5 3 4 6l-4 16c-1 2-2 3-4 3H16z" fill="#777"/></svg>
        <div>
          <h4>Our Vision</h4>
          <div class="sub">Where we are headed</div>
          <p>To be the most trusted freight partner for US manufacturers by providing reliable, honest and friendly service on every single load we move. <em>More</em></p>
        </div>
      </div>
      <div class="col">
        <svg width="54" height="54" viewBox="0 0 54 54"><circle cx="27" cy="27" r="22" fill="none" stroke="#777" stroke-width="4"/><circle cx="27" cy="27" r="13" fill="none" stroke="#777" stroke-width="4"/><circle cx="27" cy="27" r="5" fill="#777"/></svg>
        <div>
          <h4>Our Mission</h4>
          <div class="sub">What drives us daily</div>
          <p>To move our customers' freight with care and speed while building lasting relationships with shippers and carriers through clear communication. <em>More</em></p>
        </div>
      </div>
    </div>
    <span class="btn">Request a Quote</span>
  </div>
</section>

<footer class="footer-main">
  <div class="wrap">
    <div class="updates">
      <h2>Get Updates</h2>
      <p>We occasionally send out news and updates to our customers. Sign up below and be the first to hear about new lanes and services.</p>
      <div class="field">First Name*</div>
      <div class="field">Last Name*</div>
      <div class="field">Organization*</div>
      <div class="field">Email*</div>
      <span class="btn">Submit</span>
    </div>
    <div class="contact">
      <h5>Contact Info</h5>
      <ul>
        <li><span class="ic"></span>412 W. Corden Ave, Palatine, IL 60074</li>
        <li><span class="ic"></span>Office Phone: 847.555.0142</li>
        <li><span class="ic"></span>Fax: 847.555.0143</li>
        <li><span class="ic"></span>hello@brightlanefreight.com</li>
      </ul>
      <div class="support">
        <h5>Support</h5>
        <div class="badges"><div class="badge"></div><div class="badge"></div></div>
      </div>
    </div>
  </div>
  <div class="ship" role="img" aria-label="Photo of a cargo ship loaded with containers at sea"></div>
</footer>

<div class="footer-bottom">
  <div class="social"><span></span><span></span><span></span><span></span><span></span></div>
  <div class="foot-nav"><span>Home</span><span>What We Do</span><span>How We Do It</span><span>Who We Are</span><span>Tracking</span><span>Chat</span><span>Contact</span></div>
  <div class="copy">Copyright © 2015 Brightlane Freight. All rights reserved.</div>
</div>

</body>
</html>
```